On-line Christmas Card design

We are a start-up management consulting business in New Zealand and are looking for a design for an on-line Christmas card.
We want to send the "card" out by embedded into an email. We need the whole design to be seen when the email is opened so landscape is probably better.

Target Market(s)

Our clients are senior executives in public and private sector organizations.

Industry/Entity Type

Management Consulting

Requirements
Must have
• Our logo somewhere in the design. Some source files are attached which show our stationery etc. Please don't change the colors of our logo in your design.
Use of our colors - green and gray.
A generic greeting - something referring to happy holidays, seasons greetings, etc rather than "Merry Christmas".

It's summer in NZ so no winter, snow scenes. If you are proposing a photo, then beach scenes are better. We would be interested in designs that are not photos.
Should not have
• Not religious.

```html
<!DOCTYPE html>
<html lang="en">
<head>
<meta charset="utf-8">
<title>Seasons Greetings – Tarn Advisory</title>
<link rel="stylesheet" href="https://fonts.googleapis.com/css2?family=Dancing+Script:wght@600&family=Montserrat:wght@600;900&display=swap">
<style>
  :root {
    --sky-top: #5faedc;
    --sky-mid: #cfe6f2;
    --horizon: #e9f3f6;
    --sea: #37b6b4;
    --sea-deep: #1f8f9c;
    --sand: #efe6d2;
    --sand-light: #f8f3e6;
    --pine-dark: rgba(16, 58, 28, 0.95);
    --pine-soft: rgba(43, 106, 44, 0.55);
    --pine-clear: rgba(43, 106, 44, 0);
    --green-light: #a3d82c;
    --green: #6cb81c;
    --green-deep: #3f8a14;
    --white: #ffffff;
  }
  * { margin: 0; padding: 0; box-sizing: border-box; }
  html, body { width: 1200px; height: 900px; overflow: hidden; background: var(--white); }

  .card {
    position: relative;
    width: 1200px;
    height: 900px;
    overflow: hidden;
  }

  .beach-scene {
    position: absolute;
    inset: 0;
    background:
      radial-gradient(ellipse 260px 200px at 830px 470px, rgba(255,250,220,0.75), rgba(255,250,220,0) 70%),
      linear-gradient(180deg,
        var(--sky-top) 0%,
        var(--sky-mid) 38%,
        var(--horizon) 61%,
        var(--sea) 62%,
        var(--sea-deep) 70%,
        var(--sea) 75%,
        var(--sand-light) 77%,
        var(--sand) 100%);
  }

  .garland-frame {
    position: absolute;
    inset: 0;
    background:
      linear-gradient(180deg, var(--pine-dark) 0, var(--pine-soft) 90px, var(--pine-clear) 170px),
      linear-gradient(90deg, var(--pine-dark) 0, var(--pine-soft) 90px, var(--pine-clear) 170px),
      linear-gradient(270deg, var(--pine-dark) 0, var(--pine-soft) 80px, var(--pine-clear) 150px);
  }

  .greeting {
    position: absolute;
    left: 228px;
    top: 278px;
    font-weight: normal;
  }
  .greeting__script {
    display: block;
    font-family: "Dancing Script", cursive;
    font-weight: 600;
    font-size: 112px;
    line-height: 1;
    color: var(--green-light);
    text-shadow: 0 2px 6px rgba(255,255,255,0.5);
  }
  .greeting__main {
    display: block;
    margin-top: 14px;
    font-family: "Montserrat", sans-serif;
    font-weight: 900;
    font-size: 118px;
    line-height: 1;
    letter-spacing: 0;
    background: linear-gradient(180deg, var(--green-light), var(--green) 55%, var(--green-deep));
    -webkit-background-clip: text;
    background-clip: text;
    color: transparent;
  }

  .brand {
    position: absolute;
    left: 338px;
    top: 792px;
    display: flex;
    align-items: center;
    gap: 14px;
  }
  .brand__mark {
    width: 34px; height: 34px;
    background: var(--green);
  }
  .brand__name {
    font-family: "Montserrat", sans-serif;
    font-weight: 600;
    font-size: 56px;
    line-height: 1;
    color: var(--green);
  }
</style>
</head>
<body>
  <main class="card">
    <div class="beach-scene" role="img" aria-label="Sunny tropical beach with two wooden loungers under a thatched umbrella and turquoise sea"></div>

    <div class="garland-frame" role="img" aria-label="Frame of pine and holly garland with red berries, gold baubles, sparkles and a red bow with bells at the top"></div>

    <h1 class="greeting">
      <span class="greeting__script">Seasons</span>
      <span class="greeting__main">GREETINGS</span>
    </h1>

    <div class="brand">
      <span class="brand__mark"></span>
      <span class="brand__name">Tarn Advisory</span>
    </div>
  </main>
</body>
</html>
```